Lantern Care Solutions Banner Ad

Need a 750 x 250-pixel banner ad with the company Logo included. Please see company website at www.lanterncaresolutions.example for more information.

```html
<!DOCTYPE html>
<html lang="en">
<head>
<meta charset="utf-8">
<title>Lantern Care Solutions Banner Ads</title>
<link rel="stylesheet" href="https://fonts.googleapis.com/css2?family=Baloo+2:wght@400;600&family=Roboto:wght@400&family=Montserrat:wght@400;700&display=swap">
<style>
  :root {
    --navy: #17466b;
    --navy-deep: #0f4c7a;
    --green: #62ad1b;
    --ink: #1e2a22;
    --white: #ffffff;
    --page: #ffffff;
  }
  * { margin: 0; padding: 0; box-sizing: border-box; }
  html, body { width: 1103px; height: 1200px; overflow: hidden; background: var(--page); }
  .canvas { position: relative; width: 1103px; height: 1200px; }

  .banner {
    position: absolute;
    left: 44px;
    width: 750px;
    height: 250px;
    transform: scale(1.345);
    transform-origin: 0 0;
    overflow: hidden;
    background: var(--white);
    box-shadow: 0 1px 4px rgba(0,0,0,0.25);
  }
  .banner--coordination { top: 48px; }
  .banner--goals { top: 430px; }
  .banner--know { top: 811px; }

  .brand {
    position: absolute;
    display: flex;
    align-items: center;
    gap: 5px;
    font-family: "Baloo 2", sans-serif;
    font-weight: 600;
    color: var(--navy);
    white-space: nowrap;
  }
  .brand__dot { width: 12px; height: 12px; border-radius: 50%; background: var(--green); flex: none; }

  .photo { position: absolute; }

  /* Banner 1 */
  .banner--coordination .brand { left: 14px; top: 16px; font-size: 13px; }
  .banner--coordination .photo {
    left: 290px; top: 0; width: 460px; height: 250px;
    background:
      linear-gradient(90deg, #ffffff 0%, rgba(255,255,255,0) 26%),
      linear-gradient(180deg, #e9e1d6 0%, #d8c3ab 45%, #b99a7e 75%, #8d6c55 100%);
  }
  .coordination__headline {
    position: absolute; left: 73px; top: 86px;
    font-family: "Baloo 2", sans-serif; font-weight: 600;
    font-size: 25px; line-height: 38px; color: var(--navy);
  }

  /* Banner 2 */
  .banner--goals .photo {
    left: 0; top: 0; width: 403px; height: 250px;
    background: linear-gradient(160deg, #b8a58a 0%, #d9c3a4 35%, #a8474c 65%, #4a3a34 100%);
  }
  .banner--goals .brand { right: 16px; top: 20px; font-size: 13px; }
  .goals__tag {
    position: absolute; left: 379px;
    font-family: "Roboto", sans-serif; font-size: 23px;
    height: 43px; line-height: 43px; padding-left: 16px;
    white-space: nowrap;
  }
  .goals__tag--green { top: 78px; width: 260px; background: var(--green); color: var(--ink); }
  .goals__tag--navy { top: 129px; width: 355px; background: var(--navy-deep); color: var(--white); }
  .goals__copy {
    position: absolute; left: 413px; top: 179px; width: 300px;
    font-family: "Baloo 2", sans-serif; font-size: 12.5px; line-height: 22px; color: var(--navy);
  }

  /* Banner 3 */
  .banner--know { background: var(--green); }
  .banner--know .photo { left: 0; top: 0; width: 750px; height: 250px; }
  .know__headline {
    position: absolute; left: 46px; top: 72px;
    font-family: "Montserrat", sans-serif; font-weight: 700;
    font-size: 25px; color: var(--white); white-space: nowrap;
  }
  .know__copy {
    position: absolute; left: 46px; top: 110px; width: 335px;
    font-family: "Montserrat", sans-serif; font-size: 12px; line-height: 21px; color: var(--white);
  }
  .banner--know .brand { left: 12px; top: 222px; font-size: 10px; color: var(--navy); }
  .banner--know .brand__dot { width: 9px; height: 9px; background: var(--navy); }
</style>
</head>
<body>
<main class="canvas">

  <section class="banner banner--coordination">
    <div class="photo" role="img" aria-label="Photo of two women talking at a café table, one seated in a wheelchair"></div>
    <div class="brand"><span class="brand__dot"></span>Lantern Care Solutions</div>
    <h1 class="coordination__headline">Support Coordination<br>Across New Jersey</h1>
  </section>

  <section class="banner banner--goals">
    <div class="photo" role="img" aria-label="Photo of a smiling woman playing bongo drums beside a woman playing guitar"></div>
    <div class="brand"><span class="brand__dot"></span>Lantern Care Solutions</div>
    <div class="goals__tag goals__tag--green">We make your goals</div>
    <div class="goals__tag goals__tag--navy">our mission for your services</div>
    <p class="goals__copy">Our Support Coordinators focus on you; We know you are special and we want to know why.</p>
  </section>

  <section class="banner banner--know">
    <svg class="photo" width="750" height="250" viewBox="0 0 750 250" role="img" aria-label="Photo of a person in a power wheelchair on a tree-lined sidewalk">
      <defs>
        <linearGradient id="street" x1="0" y1="0" x2="0" y2="1">
          <stop offset="0" stop-color="#a9b2a6"/>
          <stop offset="0.55" stop-color="#7b8a68"/>
          <stop offset="1" stop-color="#5b6650"/>
        </linearGradient>
      </defs>
      <polygon points="440,0 750,0 750,250 378,250" fill="url(#street)"/>
      <line x1="440" y1="0" x2="378" y2="250" stroke="var(--navy-deep)" stroke-width="3"/>
    </svg>
    <h2 class="know__headline">We Get to Know You</h2>
    <p class="know__copy">Using the New Jersey Comprehensive Tool (NJCAT) completed by you, we paint a picture of where you are and want to be.</p>
    <div class="brand"><span class="brand__dot"></span>Lantern Care Solutions</div>
  </section>

</main>
</body>
</html>
```